Financial industry/Advisor business card

I'm a Financial Advisor starting my own investment company, Brandvik Wealth Management. I currently use the 'Light Blue' color that's provided on the Cardmello web page, but I want something unique. I'd like to keep the color, but the design is up for grabs.

Industry/Entity Type

Business

Contact Information for Business Card

Brandvik Wealth Management
Dale R. Brandvik
President
5142 Gableston Ln
Ste 240
Chadds Ford Pa 19402
610-555-0147-Office
610-555-0183-Fax
DBRANDVIK@BRANDVIKW.example

```html
<!DOCTYPE html>
<html lang="en">
<head>
<meta charset="utf-8">
<title>Brandvik Wealth Management – Business Cards</title>
<link rel="stylesheet" href="https://fonts.googleapis.com/css2?family=Source+Sans+3:wght@300;400;600&display=swap">
<style>
  :root {
    --stage: #141414;
    --card-white: #ffffff;
    --card-grey: #878787;
    --card-blue: #45b8e9;
    --brand-blue: #3fb3e6;
    --text-dark: #3c3c3c;
    --mark-grey: #8a8a8a;
    --on-colour: #ffffff;
  }
  * { margin: 0; padding: 0; box-sizing: border-box; }
  html, body { width: 1200px; height: 900px; overflow: hidden; }
  body {
    background: var(--stage);
    font-family: "Source Sans 3", sans-serif;
    position: relative;
  }
  .card {
    position: absolute;
    width: 451px;
    height: 261px;
    border-radius: 12px;
  }
  .card--front { background: var(--card-white); left: 131px; }
  .card--back { left: 610px; width: 455px; height: 263px; }
  .card--back.is-grey { background: var(--card-grey); }
  .card--back.is-blue { background: var(--card-blue); }
  .row-top { top: 174px; }
  .row-bottom { top: 498px; }

  .brand {
    position: absolute;
    text-align: center;
    font-weight: 300;
    line-height: 1;
  }
  .brand__dot {
    display: block;
    margin: 0 auto 14px;
    width: 22px; height: 22px;
    border-radius: 50%;
  }
  .brand__name { display: block; font-size: 44px; letter-spacing: -0.5px; }
  .brand__tag { display: block; font-size: 17px; margin-top: 2px; }

  .card--front .brand { left: 20px; width: 215px; top: 80px; color: var(--brand-blue); }
  .card--front .brand__dot { background: var(--mark-grey); }
  .card--back .brand { left: 0; width: 100%; top: 88px; color: var(--on-colour); }
  .card--back .brand__name { font-size: 48px; }
  .card--back .brand__dot { background: var(--on-colour); }

  .contact {
    position: absolute;
    left: 218px;
    top: 48px;
    color: var(--text-dark);
    font-size: 13.5px;
    line-height: 14.5px;
  }
  .contact__name {
    color: var(--brand-blue);
    font-weight: 600;
    font-size: 20px;
    line-height: 24px;
  }
  .contact__title { margin-top: 1px; }
  .contact__address { margin-top: 12px; }
  .contact__list { list-style: none; margin-top: 14px; }
  .contact__list li { display: flex; align-items: center; height: 17px; }
  .contact__list svg { width: 9px; height: 9px; margin: 0 9px 0 3px; fill: var(--brand-blue); stroke: var(--brand-blue); }
</style>
</head>
<body>

<!-- Front, top row -->
<section class="card card--front row-top">
  <div class="brand">
    <span class="brand__dot"></span>
    <span class="brand__name">Brandvik</span>
    <span class="brand__tag">Wealth Management</span>
  </div>
  <div class="contact">
    <p class="contact__name">Jonathan Smith</p>
    <p class="contact__title">Managing Director</p>
    <p class="contact__address">1234, Address Goes Here<br>Country Name, 123456</p>
    <ul class="contact__list">
      <li><svg viewBox="0 0 10 10"><rect x="2.5" y="0.5" width="5" height="9" rx="1" fill="none" stroke-width="1.2"/></svg>123-456-7890</li>
      <li><svg viewBox="0 0 10 10"><path d="M0 4 Q5 0 10 4 L8 5 L7 3.5 Q5 3 3 3.5 L2 5 Z" stroke="none"/><rect x="2" y="6" width="6" height="3" stroke="none"/></svg>123-456-7890</li>
      <li><svg viewBox="0 0 10 10"><rect x="1" y="3" width="8" height="6" stroke="none"/><rect x="3" y="0.5" width="4" height="3" fill="none" stroke-width="1"/></svg>123-456-7890</li>
      <li><svg viewBox="0 0 10 10"><rect x="0.5" y="2" width="9" height="6" stroke="none"/></svg>info@brandvikw.example</li>
      <li><svg viewBox="0 0 10 10"><path d="M2 8 L8 2" fill="none" stroke-width="1.2"/><circle cx="7.5" cy="2.5" r="1.8" fill="none" stroke-width="1"/><circle cx="2.5" cy="7.5" r="1.8" fill="none" stroke-width="1"/></svg>www.brandvikw.example</li>
    </ul>
  </div>
</section>

<!-- Back, grey -->
<section class="card card--back is-grey row-top">
  <div class="brand">
    <span class="brand__dot"></span>
    <span class="brand__name">Brandvik</span>
    <span class="brand__tag">Wealth Management</span>
  </div>
</section>

<!-- Front, bottom row -->
<section class="card card--front row-bottom">
  <div class="brand">
    <span class="brand__dot"></span>
    <span class="brand__name">Brandvik</span>
    <span class="brand__tag">Wealth Management</span>
  </div>
  <div class="contact">
    <p class="contact__name">Jonathan Smith</p>
    <p class="contact__title">Managing Director</p>
    <p class="contact__address">1234, Address Goes Here<br>Country Name, 123456</p>
    <ul class="contact__list">
      <li><svg viewBox="0 0 10 10"><rect x="2.5" y="0.5" width="5" height="9" rx="1" fill="none" stroke-width="1.2"/></svg>123-456-7890</li>
      <li><svg viewBox="0 0 10 10"><path d="M0 4 Q5 0 10 4 L8 5 L7 3.5 Q5 3 3 3.5 L2 5 Z" stroke="none"/><rect x="2" y="6" width="6" height="3" stroke="none"/></svg>123-456-7890</li>
      <li><svg viewBox="0 0 10 10"><rect x="1" y="3" width="8" height="6" stroke="none"/><rect x="3" y="0.5" width="4" height="3" fill="none" stroke-width="1"/></svg>123-456-7890</li>
      <li><svg viewBox="0 0 10 10"><rect x="0.5" y="2" width="9" height="6" stroke="none"/></svg>info@brandvikw.example</li>
      <li><svg viewBox="0 0 10 10"><path d="M2 8 L8 2" fill="none" stroke-width="1.2"/><circle cx="7.5" cy="2.5" r="1.8" fill="none" stroke-width="1"/><circle cx="2.5" cy="7.5" r="1.8" fill="none" stroke-width="1"/></svg>www.brandvikw.example</li>
    </ul>
  </div>
</section>

<!-- Back, blue -->
<section class="card card--back is-blue row-bottom">
  <div class="brand">
    <span class="brand__dot"></span>
    <span class="brand__name">Brandvik</span>
    <span class="brand__tag">Wealth Management</span>
  </div>
</section>

</body>
</html>
```